Marroway Commercial Crushing and Screening

Need Truck, van wrap design, with our logo. For Kelbo Tarven 35 Long Wheelbase (LWB) High Roof, Dimensions (LWB): 6,836 mm total vehicle length with a 4,300 mm load length. Roof Height: 2,196 mm height.
And for Truck Curtain 2.4m height and 4.92m length, 60cm margin from the bottom for buckles ( can't be writing) picture allowed
Updates

Need extra days to review

Sick

Industry/Entity Type

Mobile Crushing and screening

Colors

Designer to choose colors to be used in the design.

Requirements
Must have
• logo, phone number, words MOBILE CRUSHING AND SCREENING, colours as in logo, must list what we crush and screen as per flyer attached
Nice to have
• maybe crushed rocks as a back ground

```html
<!DOCTYPE html>
<html lang="en">
<head>
<meta charset="utf-8">
<title>Marroway Commercial – Van Wrap Artwork</title>
<link href="https://fonts.googleapis.com/css2?family=Poppins:wght@600;700;800&display=swap" rel="stylesheet">
<style>
  :root {
    --green-dark: #17683a;
    --green-light: #8dc045;
    --white: #ffffff;
    --panel-white: #f4f5f4;
    --outline: #d7dad8;
    --rock-light: #b3b3b0;
    --rock-dark: #4e4f4d;
    --ink: #1a1a1a;
  }
  * { margin: 0; padding: 0; box-sizing: border-box; }
  html, body {
    width: 1200px; height: 1199px; overflow: hidden;
    background: var(--white);
    font-family: "Poppins", sans-serif;
  }
  .canvas { position: relative; width: 1200px; height: 1199px; }

  .wrap-panel { position: absolute; overflow: hidden; }
  .wrap-panel svg.panel-shapes { position: absolute; inset: 0; width: 100%; height: 100%; }

  /* Side */
  .side-panel { left: 112px; top: 100px; width: 1030px; height: 350px; border-radius: 60px 14px 10px 40px; }
  .side-headline { position: absolute; left: 672px; width: 240px; text-align: center; font-weight: 800; line-height: 1; letter-spacing: -0.5px; }
  .side-headline .line { display: block; font-size: 37px; margin-bottom: 8px; }
  .side-headline .white { color: var(--white); }
  .side-headline .lime { color: var(--green-light); }
  .service-list { position: absolute; top: 170px; list-style: none; color: var(--white); font-weight: 700; font-size: 14.5px; line-height: 20px; }
  .service-list li::before { content: "• "; }
  .service-list.col-a { left: 612px; }
  .service-list.col-b { left: 741px; }
  .side-phone { position: absolute; left: 373px; top: 236px; font-weight: 700; font-size: 33px; color: var(--white); letter-spacing: -0.5px; }
  .side-phone .lime { color: var(--green-light); }

  /* Name mark */
  .name-mark { position: absolute; display: flex; align-items: center; gap: 8px; }
  .name-mark .dot { border-radius: 50%; flex: none; }
  .name-mark .name { font-weight: 800; line-height: 1.05; text-transform: uppercase; }
  .side-mark { left: 366px; top: 108px; }
  .side-mark .dot { width: 20px; height: 20px; background: var(--green-light); }
  .side-mark .name { color: var(--green-dark); font-size: 22px; }

  /* Front */
  .front-panel { left: 127px; top: 602px; width: 476px; height: 534px; background: var(--panel-white); border: 1px solid var(--outline); border-radius: 70px 70px 30px 30px; }
  .front-mark { left: 138px; top: 216px; }
  .front-mark .dot { width: 14px; height: 14px; background: var(--green-light); }
  .front-mark .name { color: var(--green-dark); font-size: 17px; }

  /* Rear */
  .rear-panel { left: 640px; top: 593px; width: 456px; height: 430px; border-radius: 8px 8px 4px 4px; }
  .rear-tagline { position: absolute; top: 8px; width: 100%; text-align: center; color: var(--white); font-weight: 700; font-size: 15.5px; }
  .rear-phone { position: absolute; top: 30px; width: 100%; text-align: center; color: var(--white); font-weight: 700; font-size: 40px; letter-spacing: -0.5px; }
  .rear-mark { left: 60px; top: 150px; }
  .rear-mark .dot { width: 30px; height: 30px; background: var(--white); }
  .rear-mark .name { color: var(--white); font-size: 32px; }
</style>
</head>
<body>
<main class="canvas">

  <!-- Side elevation -->
  <section class="wrap-panel side-panel">
    <svg class="panel-shapes" viewBox="0 0 1030 350" preserveAspectRatio="none">
      <defs>
        <linearGradient id="rockSide" x1="0" y1="0" x2="1" y2="1">
          <stop offset="0" stop-color="var(--rock-light)"/>
          <stop offset="1" stop-color="var(--rock-dark)"/>
        </linearGradient>
      </defs>
      <rect class="body-white" width="1030" height="350" fill="var(--panel-white)"/>
      <path class="sweep-dark" fill="var(--green-dark)"
        d="M0,300 C90,262 220,250 366,240 C520,232 560,140 640,60 C680,22 720,16 770,16 L1030,12 L1030,350 L0,350 Z"/>
      <path class="corner-lime" fill="var(--green-light)"
        d="M1030,80 C970,90 935,140 928,200 L930,290 L1030,290 Z"/>
      <g role="img" aria-label="Pile of crushed grey rock">
        <path fill="url(#rockSide)" d="M752,280 C780,240 820,200 880,170 C930,140 980,140 1030,135 L1030,285 L752,285 Z"/>
      </g>
      <rect class="stripe-dark" x="0" y="288" width="1030" height="34" fill="var(--ink)" opacity="0.9"/>
      <path class="stripe-lime" fill="var(--green-light)" d="M205,322 L770,322 L770,345 L190,345 Z"/>
    </svg>

    <div class="name-mark side-mark">
      <span class="dot"></span>
      <span class="name">Marroway<br>Commercial</span>
    </div>

    <h2 class="side-headline" style="top:26px">
      <span class="line white">MOBILE</span>
      <span class="line lime">CRUSHING &amp;</span>
      <span class="line white">SCREENING</span>
    </h2>

    <ul class="service-list col-a">
      <li>Brick</li><li>Concrete</li><li>Natural Stone</li><li>Blocks</li>
    </ul>
    <ul class="service-list col-b">
      <li>Asphalt</li><li>Gravel</li><li>Soil</li><li>Sand</li>
    </ul>

    <p class="side-phone">042 <span class="lime">555</span> 0198</p>
  </section>

  <!-- Front elevation -->
  <section class="wrap-panel front-panel">
    <div class="name-mark front-mark">
      <span class="dot"></span>
      <span class="name">Marroway<br>Commercial</span>
    </div>
  </section>

  <!-- Rear elevation -->
  <section class="wrap-panel rear-panel">
    <svg class="panel-shapes" viewBox="0 0 456 430" preserveAspectRatio="none">
      <defs>
        <linearGradient id="rockRear" x1="0" y1="0" x2="0" y2="1">
          <stop offset="0" stop-color="var(--rock-light)"/>
          <stop offset="1" stop-color="var(--rock-dark)"/>
        </linearGradient>
      </defs>
      <rect width="456" height="430" fill="var(--green-dark)"/>
      <path class="lime-field" fill="var(--green-light)"
        d="M0,105 C40,82 80,80 140,80 L320,80 C380,80 420,82 456,105 L456,300 C400,290 380,285 350,280 L100,280 C70,285 40,290 0,300 Z"/>
      <g role="img" aria-label="Crushed grey rock piles at the lower corners">
        <path fill="url(#rockRear)" d="M0,255 C60,250 100,270 140,300 C180,330 210,360 228,400 L228,430 L0,430 Z"/>
        <path fill="url(#rockRear)" d="M456,255 C396,250 356,270 316,300 C276,330 246,360 228,400 L228,430 L456,430 Z"/>
      </g>
    </svg>

    <p class="rear-tagline">MOBILE CRUSHING &amp; SCREENING</p>
    <p class="rear-phone">042 555 0198</p>

    <div class="name-mark rear-mark">
      <span class="dot"></span>
      <span class="name">Marroway<br>Commercial</span>
    </div>
  </section>

</main>
</body>
</html>
```